2 Business Card Designs

Need two business cards designed:
1) for lumora films (wedding video) website is lumorafilms.com.au
2) for lumora films (corporate video) website is lumorafilms.net.au

I am looking for something simple, no fancy shapes etc. Just elegant, simple and classy.

Both companies are video companies, one specialising in weddings the other corporate videos. Neither card needs to have any pics of video or camera related images. Please use same colour schemes as respective websites.

Logo is the same but can change colour.

Industry/Entity Type

Camera

Requirements
Must have
• Logo should be either all white or a colour to match websites
Should not have
• swirls, flowers, shapes, etc.

```html
<!DOCTYPE html>
<html lang="en">
<head>
<meta charset="utf-8">
<title>lumora films – business cards</title>
<link rel="stylesheet" href="https://fonts.googleapis.com/css2?family=Ubuntu:wght@300;400&display=swap">
<style>
  :root {
    --backdrop: #e9e6e1;
    --card-cream: #dfe3c8;
    --olive: #6a6d5c;
    --olive-text: #656857;
    --charcoal: #414141;
    --charcoal-text: #454545;
    --small-text: #5f6254;
    --white: #ffffff;
  }
  * { margin: 0; padding: 0; box-sizing: border-box; }
  html, body {
    width: 1200px;
    height: 900px;
    overflow: hidden;
    background: var(--backdrop);
    font-family: "Ubuntu", sans-serif;
  }
  .canvas { position: relative; width: 1200px; height: 900px; }

  .card {
    position: absolute;
    width: 532px;
    height: 304px;
    box-shadow: 0 2px 6px rgba(0,0,0,0.18);
    overflow: hidden;
  }
  .card--front { background: var(--card-cream); left: 37px; }
  .card--back { left: 634px; }
  .row-wedding { top: 134px; }
  .row-corporate { top: 462px; }
  .card--back.olive { background: var(--olive); }
  .card--back.charcoal { background: var(--charcoal); }

  .top-band { position: absolute; left: 0; top: 0; width: 100%; height: 12px; }
  .olive .top-band, .theme-olive .top-band { background: var(--olive); }
  .theme-charcoal .top-band { background: var(--charcoal); }

  .wordmark {
    font-weight: 300;
    letter-spacing: 0.5px;
    white-space: nowrap;
  }
  .card--front .wordmark {
    position: absolute;
    right: 30px;
    top: 26px;
    font-size: 46px;
  }
  .theme-olive .wordmark { color: var(--olive-text); }
  .theme-charcoal .wordmark { color: var(--charcoal-text); }

  .holder-name {
    position: absolute;
    left: 25px;
    top: 196px;
    font-size: 25px;
    font-weight: 400;
  }
  .theme-olive .holder-name { color: var(--olive-text); }
  .theme-charcoal .holder-name { color: var(--charcoal-text); }

  .name-rule {
    position: absolute;
    left: 0;
    top: 230px;
    width: 232px;
    height: 10px;
  }

  .contact {
    position: absolute;
    left: 25px;
    top: 249px;
    font-size: 11px;
    line-height: 17px;
    color: var(--small-text);
  }

  .card--back .wordmark {
    position: absolute;
    left: 0;
    right: 0;
    top: 110px;
    text-align: center;
    font-size: 46px;
    color: var(--white);
  }
  .website {
    position: absolute;
    left: 0;
    right: 0;
    top: 198px;
    text-align: center;
    font-size: 15px;
    font-weight: 300;
    letter-spacing: 0.4px;
    color: var(--white);
  }
</style>
</head>
<body>
<main class="canvas">

  <!-- Wedding video: front -->
  <section class="card card--front row-wedding theme-olive">
    <div class="top-band"></div>
    <div class="wordmark">lumora films</div>
    <h2 class="holder-name">Mara Ellison</h2>
    <svg class="name-rule" viewBox="0 0 232 10" aria-hidden="true">
      <line x1="0" y1="5" x2="224" y2="5" stroke="#6a6d5c" stroke-width="2"/>
      <circle cx="225" cy="5" r="4.5" fill="#6a6d5c"/>
    </svg>
    <p class="contact">Carrow Vale :: NSW :: 2099<br>Phone: +61 2 5550 1842</p>
  </section>

  <!-- Wedding video: back -->
  <section class="card card--back row-wedding olive">
    <div class="wordmark">lumora films</div>
    <p class="website">www.lumorafilms.com.au</p>
  </section>

  <!-- Corporate video: front -->
  <section class="card card--front row-corporate theme-charcoal">
    <div class="top-band"></div>
    <div class="wordmark">lumora films</div>
    <h2 class="holder-name">Mara Ellison</h2>
    <svg class="name-rule" viewBox="0 0 232 10" aria-hidden="true">
      <line x1="0" y1="5" x2="224" y2="5" stroke="#5a5a5a" stroke-width="2"/>
      <circle cx="225" cy="5" r="4.5" fill="#5a5a5a"/>
    </svg>
    <p class="contact">Carrow Vale :: NSW :: 2099<br>Phone: +61 2 5550 1842</p>
  </section>

  <!-- Corporate video: back -->
  <section class="card card--back row-corporate charcoal">
    <div class="wordmark">lumora films</div>
    <p class="website">www.lumorafilms.net.au</p>
  </section>

</main>
</body>
</html>
```